Stylish High End Wedding Videography/Films Website (BDMR)

We need a modern and high-end website look for our wedding video and films business. We films weddings all over the United Kingdom and at European destinations so need something to reflect our work. The website should be visually stunning with images and videos being the focal point as this is what our services are;

I have uploads of some items I like and the features the site needs to have. These have been taken from other websites using standout features.

We need the following pages;

1 - Homepage
2 - Films Index Page
3 - Individual Films Page
4 - Prices / Collection Page
5 - Reviews
6 - Options
7 - About
8 - Contact
9 - Blog Index
10 - Blog Page

All pages must be consistent so have a similar style.

Pages on menu:
Films
Prices
Reviews
Options
About
Contact

We require a responsive look too. Over 90% of our visitors access the website via their mobile devices.

Please use the colours from our logo to incorporate into the website.

Target Market(s)

Wedding Couples

Industry/Entity Type

Wedding Photography

Number of Pages Required

5+ page

Font styles to use
Sans Serif
Script

Requirements
Must have
• The logo must be in the centre of the menu at the top.

Social icons at the bottom of the page.

Use only two fonts including Lore which is supplied
Nice to have
• Different video for each page on the top header. This will play behind the menu.

```html
<!DOCTYPE html>
<html lang="en">
<head>
<meta charset="utf-8">
<title>Bram Delmar Wedding Films</title>
<link href="https://fonts.googleapis.com/css2?family=Jost:wght@400;500&family=Raleway:ital,wght@0,400;1,400&display=swap" rel="stylesheet">
<style>
:root{
  --ink:#1f1c18;
  --white:#ffffff;
  --gold:#c9a86a;
  --brown:#6b5b3e;
  --grey-bg:#f2f2f2;
  --text-grey:#777;
  --line:#d9d9d9;
}
*{margin:0;padding:0;box-sizing:border-box}
html,body{width:1200px;height:3360px;overflow:hidden;background:var(--white)}
body{position:relative;font-family:'Raleway',sans-serif;color:var(--ink)}
.abs{position:absolute}
.head{font-family:'Jost',sans-serif;font-weight:500;letter-spacing:.02em;text-transform:uppercase}

/* hero */
.hero{left:0;top:0;width:1200px;height:600px;background:linear-gradient(90deg,#0c0e0b 0%,#1a1d17 45%,#5a5043 60%,#2d3446 85%,#1c2233 100%)}
.nav a{position:absolute;top:73px;font-family:'Jost',sans-serif;font-size:16px;color:var(--white);text-decoration:none;text-transform:uppercase}
.nav a.active{color:var(--gold)}
.brand{left:540px;top:24px;width:170px;text-align:center;color:var(--white)}
.brand .mark{width:30px;height:30px;border:2px solid var(--gold);margin:0 auto 8px}
.brand .name{font-family:'Jost',sans-serif;font-size:15px;letter-spacing:.2em}
.brand .sub{font-family:'Jost',sans-serif;font-size:7px;letter-spacing:.4em}
.hero-title{left:112px;top:250px;font-size:56px;color:var(--white)}
.hero-sub{left:112px;top:322px;font-size:16px;color:var(--white)}
.hero-rule{left:0;top:489px;width:1200px;height:1px;background:rgba(255,255,255,.3)}
.scroll{left:112px;top:527px;font-size:16px;color:var(--white);display:flex;gap:8px;align-items:center}
.slides{left:818px;top:527px;display:flex;gap:17px;font-family:'Jost',sans-serif;font-size:15px;color:rgba(255,255,255,.7)}
.slides span.on{color:var(--white);border-bottom:1px solid var(--white);padding-bottom:4px}

.intro{left:160px;top:696px;width:880px;text-align:center;font-style:italic;font-size:15px;line-height:32px;color:var(--text-grey)}

/* photos */
.photos{left:0;top:888px;width:1192px;height:952px;background:var(--grey-bg)}
.sec-title{left:0;top:935px;width:1184px;text-align:center;font-size:42px}
.view-all{left:985px;top:952px;font-family:'Jost',sans-serif;font-size:16px;color:var(--brown);text-decoration:underline;display:flex;gap:14px;align-items:center}
.ph{position:absolute}
.cap-in{position:absolute;left:20px;bottom:22px;color:var(--white);font-size:15px;line-height:27px}
.cap{position:absolute;font-size:15px;line-height:27px;color:var(--ink)}

/* video */
.arrows{left:111px;top:2002px;display:flex;gap:20px}
.video{left:368px;top:1942px;width:720px;height:482px;background:linear-gradient(160deg,#b35a2c 0%,#5c4a33 35%,#8a8779 60%,#4e5638 100%)}
.play{left:688px;top:2142px;width:82px;height:82px;border-radius:50%;background:rgba(70,55,35,.85)}
.card{left:113px;top:2050px;width:376px;height:450px;background:var(--white);box-shadow:0 0 6px rgba(0,0,0,.12);text-align:center;padding-top:100px}
.card h3{font-size:25px;line-height:33px}
.card p{margin:22px 20px 0;font-size:15px;line-height:33px;color:var(--text-grey)}
.btn{display:inline-block;margin-top:14px;width:153px;height:50px;line-height:50px;background:var(--brown);color:var(--white);font-family:'Jost',sans-serif;font-size:16px}

/* reviews */
.reviews{left:0;top:2608px;width:1200px;height:325px;background:linear-gradient(180deg,#2a2a22,#3b3a2d 50%,#26261f);color:var(--white);text-align:center}
.reviews h2{margin-top:50px;font-size:42px}
.reviews .quote{margin:14px auto 0;width:900px;font-style:italic;font-size:15px;line-height:32px}
.reviews .who{margin-top:14px;font-family:'Jost',sans-serif;font-size:15px}
.reviews .where{margin-top:4px;font-size:12px}

/* footer */
.fcol{top:3030px;text-align:center}
.fcol h4{font-family:'Jost',sans-serif;font-weight:400;font-size:32px;letter-spacing:.04em;color:var(--brown)}
.fcol p{margin-top:10px;font-size:16px;line-height:27px;color:var(--text-grey)}
.fdiv{top:3015px;width:1px;height:175px;background:var(--line)}
.social{display:flex;gap:22px;justify-content:center;margin-top:28px}
.social span{width:14px;height:14px;border-radius:50%;background:var(--brown)}
.fnav{left:0;top:3224px;width:1200px;display:flex;justify-content:center;gap:0}
.fnav a{font-family:'Jost',sans-serif;font-size:16px;color:var(--brown);text-decoration:none;margin:0 27px}
.frule{left:111px;top:3266px;width:977px;height:1px;background:var(--ink)}
.badge{left:105px;top:3275px;width:64px;height:64px;border-radius:50%;background:#f3e9a8;border:2px solid #b39a55}
.copy{left:0;top:3296px;width:1200px;text-align:center;font-size:15px;color:var(--text-grey)}
.totop{left:1020px;top:3296px;font-size:15px;color:var(--text-grey);display:flex;gap:8px;align-items:center}
</style>
</head>
<body>

<div class="abs hero" role="img" aria-label="Bride and groom embracing at dusk, bride in lace gown and veil"></div>
<nav class="nav">
  <a class="active" style="left:158px">Home</a>
  <a style="left:244px">Films</a>
  <a style="left:327px">Prices</a>
  <a style="left:417px">Reviews</a>
  <a style="left:769px">Options</a>
  <a style="left:875px">About</a>
  <a style="left:966px">Contact</a>
</nav>
<div class="abs brand">
  <div class="mark"></div>
  <div class="name">BDMR</div>
  <div class="sub">WEDDING FILMS</div>
</div>
<h1 class="abs head hero-title">Bram Delmar</h1>
<p class="abs hero-sub">WEDDING VIDEOGRAPHY - NORTH EAST, UK AND WORLDWIDE FILMS</p>
<div class="abs hero-rule"></div>
<div class="abs scroll">
  <svg width="14" height="22" viewBox="0 0 14 22"><path d="M7 0v20M1 14l6 6 6-6" fill="none" stroke="#fff" stroke-width="1.4"/></svg>
  SCROLL TO EXPLORE
</div>
<div class="abs slides"><span class="on">01</span><span>02</span><span>03</span><span>04</span><span>05</span><span>06</span><span>07</span><span>08</span></div>

<p class="abs intro">Bram Delmar is a wedding filmmaker based in the North East of England. We film weddings in a fun and natural way. All weddings are totally unique to the couple. If you are looking for a wedding film for your special<br>day we'd love to hear from you.</p>

<section class="abs photos"></section>
<h2 class="abs head sec-title">Series of Photos</h2>
<a class="abs view-all">VIEW ALL
  <svg width="16" height="12" viewBox="0 0 16 12"><path d="M0 6h15M10 1l5 5-5 5" fill="none" stroke="#6b5b3e" stroke-width="1.4"/></svg></a>

<div class="ph" style="left:111px;top:1003px;width:643px;height:429px;background:linear-gradient(180deg,#8a8a8a,#3a3a3a 60%,#cfcfcf)" role="img" aria-label="Black and white photo of a couple at a church altar">
  <div class="cap-in head">Rosie + Tom<br>Harrowmere, Northumberland</div></div>
<div class="ph" style="left:769px;top:1003px;width:317px;height:429px;background:linear-gradient(150deg,#c8582a,#e6a37a 50%,#ddd6d0)" role="img" aria-label="Smiling bride held by groom in autumn colours">
  <div class="cap-in head">Ellie + Mark<br>Ashcombe Hall, Northumberland</div></div>
<div class="ph" style="left:111px;top:1444px;width:317px;height:257px;background:linear-gradient(160deg,#7e7460,#2f3038 55%,#c9c4b8)" role="img" aria-label="Couple kissing in front of an Italian abbey"></div>
<div class="ph" style="left:442px;top:1444px;width:316px;height:257px;background:linear-gradient(120deg,#2a2e22,#2b3452 50%,#c8a57e)" role="img" aria-label="Couple touching foreheads outdoors"></div>
<div class="ph" style="left:772px;top:1444px;width:316px;height:257px;background:linear-gradient(120deg,#e5ded2,#c9b9a4 50%,#3c3c3f)" role="img" aria-label="Bride in veil with groom leaning in"></div>
<div class="cap head" style="left:113px;top:1714px">Amara + Joel<br>Badia Sant'Elmo, Colle, Italy</div>
<div class="cap head" style="left:443px;top:1714px">Hannah + Liam<br>Brindlecote Manor, Leicestershire</div>
<div class="cap head" style="left:772px;top:1714px">Megan + Ryan<br>The Grey Stag, Durham</div>

<div class="abs arrows">
  <svg width="22" height="14" viewBox="0 0 22 14"><path d="M22 7H2M8 1L2 7l6 6" fill="none" stroke="#1f1c18" stroke-width="1.6"/></svg>
  <svg width="22" height="14" viewBox="0 0 22 14"><path d="M0 7h20M14 1l6 6-6 6" fill="none" stroke="#1f1c18" stroke-width="1.6"/></svg>
</div>
<div class="abs video" role="img" aria-label="Groom kissing bride in a meadow with autumn trees"></div>
<div class="abs play"><svg width="82" height="82" viewBox="0 0 82 82"><path d="M34 29l18 12-18 12z" fill="#fff"/></svg></div>
<div class="abs card">
  <h3 class="head">Prefer something a bit<br>more funky?</h3>
  <p>If you are a couple who prefers something a bit different to the styles above then why not go for our alternative option.</p>
  <span class="btn">WATCH VIDEO</span>
</div>

<section class="abs reviews" role="img" aria-label="Aerial view of an old stone abbey among trees">
  <h2 class="head">Rviews</h2>
  <p class="quote">One of the best decisions We made was choosing you guys to film our wedding! It's absolutely fantastic, it has everyone so emotional watching it, we can't thank you enough for capturing our special day! You were amazing from start to finish Thanks so much.</p>
  <p class="who">JODIE AND MARCUS</p>
  <p class="where">The Grey Stag</p>
</section>
<svg class="abs" style="left:94px;top:2761px" width="12" height="22" viewBox="0 0 12 22"><path d="M10 1L1 11l9 10" fill="none" stroke="#fff" stroke-width="1.4"/></svg>
<svg class="abs" style="left:1096px;top:2761px" width="12" height="22" viewBox="0 0 12 22"><path d="M2 1l9 10-9 10" fill="none" stroke="#fff" stroke-width="1.4"/></svg>

<div class="abs fcol" style="left:100px;width:170px"><h4>LETS CHAT</h4><p>Send me a message</p></div>
<div class="abs fdiv" style="left:341px"></div>
<div class="abs fcol" style="left:400px;width:312px"><h4>BDMR</h4><p>We are a Stylish High End Wedding<br>Videography/Films company</p></div>
<div class="abs fdiv" style="left:769px"></div>
<div class="abs fcol" style="left:840px;width:265px"><h4>FOLLOW ALONG</h4>
  <div class="social" aria-label="Social links"><span></span><span></span><span></span><span></span></div></div>

<nav class="abs fnav"><a>HOME</a><a>FILMS</a><a>PRICES</a><a>REVIEWS</a><a>OPTIONS</a><a>ABOUT</a><a>CONTACT</a></nav>
<div class="abs frule"></div>
<div class="abs badge"></div>
<p class="abs copy">© 2020 All RightsReserved</p>
<div class="abs totop">To Top <svg width="11" height="8" viewBox="0 0 11 8"><path d="M0 8L5.5 0 11 8z" fill="#6b5b3e"/></svg></div>

</body>
</html>
```